IT Consulting Site Revamping for Marlune

I've put a skeleton together on my website, but realize I need some help (it's http://pilot.marlune-example.ca).
I've pulled together tidbits from other websites, but really need my site to be cleaned up, and really spruced up.
I primarily focus on the IT needs of small to medium size businesses, taking care of everything from their servers and networks down to their workstations.
I also want a page listing the vendors (and logos) that I work with including Quillsoft, Zentrix, Halvor, Brax, TL, RZO, VELK, Trevo, Gatemoor.
There should also be a simple form to get a quote that will email me.
The final design should communicate strength and reliability.
I would like this to be a fully functional website, that I can upload to Plumly Pages, with the same sort of pages that are existing on http://pilot.marlune-example.ca
Updates
Hey everyone,
Hi everyone,
Reason: Hi all,
There are some designers that would like to submit some new designs, so I'm extending the deadline.
Thanks,
Target Market(s)
Small to medium size business owners. This will primarily be males who work in the oil and gas industry.
Industry/Entity Type
Consulting
Look and feel
Each slider illustrates characteristics of the customer's brand and the style your logo design should communicate.

```html
<!DOCTYPE html>
<html lang="en">
<head>
<meta charset="utf-8">
<title>Marlune Solutions</title>
<link rel="stylesheet" href="https://fonts.googleapis.com/css2?family=Open+Sans:wght@400;600;700&family=Ubuntu:wght@400;500&display=swap">
<style>
:root{
  --blue-deep:#14508f;
  --blue-mid:#1f6fb6;
  --blue-light:#3c95d6;
  --brand:#1f78bd;
  --accent:#2a8fd3;
  --btn:#1b84c8;
  --btn-dark:#136aa6;
  --text:#4a4a4a;
  --heading:#444;
  --nav:#5a5a5a;
  --page-bg:#ececec;
  --panel:#ffffff;
  --field:#f7f7f7;
  --field-line:#cfcfcf;
  --badge-grey:#8c8c8c;
}
*{box-sizing:border-box;margin:0;padding:0}
html,body{width:965px;height:1200px;overflow:hidden}
body{position:relative;background:var(--page-bg);font-family:"Open Sans",Arial,sans-serif;color:var(--text)}

.hero{position:absolute;left:0;top:0;width:965px;height:437px;
  background:radial-gradient(ellipse 420px 300px at 760px 110px,rgba(120,190,240,.45),transparent 70%),
  linear-gradient(180deg,var(--blue-mid) 0%,var(--blue-deep) 100%);}
.hero-photo{position:absolute;left:260px;top:115px;width:630px;height:322px;
  background:linear-gradient(90deg,rgba(20,70,130,0) 0%,rgba(40,40,50,.35) 40%,rgba(50,45,50,.55) 75%,rgba(30,60,110,.25) 100%);}
.hero-strip{position:absolute;left:0;top:437px;width:965px;height:13px;background:#fff}

.site-header{position:absolute;left:65px;top:0;width:839px;height:101px;background:linear-gradient(180deg,#fff,#f1f4f8);
  border-radius:0 0 14px 14px;box-shadow:0 2px 6px rgba(0,0,0,.2)}
.brand{position:absolute;left:37px;top:26px;display:flex;align-items:center;gap:10px}
.brand-mark{width:44px;height:44px;border-radius:50%;background:var(--brand)}
.brand-name{font-weight:700;font-size:32px;color:var(--brand);letter-spacing:-.5px;line-height:1}
.main-nav{position:absolute;top:44px;left:336px;display:flex;gap:18px;font-weight:700;font-size:14px;color:var(--nav)}
.main-nav a{color:inherit;text-decoration:none}
.main-nav a.current{color:var(--brand)}

.hero-copy{position:absolute;left:91px;top:157px;font-family:Ubuntu,sans-serif;font-size:18px;line-height:29px;color:#fff;text-shadow:0 1px 2px rgba(0,0,0,.25)}
.more-btn{position:absolute;left:91px;top:228px;width:60px;height:29px;border-radius:5px;background:linear-gradient(180deg,#4a9ad4,#2b74b3);
  font-family:Ubuntu,sans-serif;font-size:15px;color:#fff;display:flex;align-items:center;justify-content:center;box-shadow:0 1px 2px rgba(0,0,0,.3)}

.values{position:absolute;left:0;top:380px}

.content-panel{position:absolute;left:63px;top:535px;width:841px;height:555px;background:var(--panel);border-radius:20px}
.welcome{position:absolute;left:29px;top:30px;width:489px}
.section-title{font-size:15px;font-weight:600;color:var(--heading);padding-bottom:4px}
.welcome .section-title{border-bottom:1px solid #d6d6d6}
.welcome-text{margin-top:8px;padding-left:2px;font-size:10.4px;line-height:16.1px;text-align:justify;color:var(--text)}

.quote{position:absolute;left:546px;top:30px;width:258px}
.field{display:block;width:256px;height:32px;margin-top:10px;border:1px solid var(--field-line);border-radius:6px;background:var(--field);
  font-size:10.5px;color:#777;padding:9px 8px;font-family:inherit;box-shadow:inset 0 1px 2px rgba(0,0,0,.08)}
.quote .section-title{margin-bottom:2px}
.field.area{height:193px}
.form-actions{display:flex;gap:9px;margin-top:15px}
.btn{width:83px;height:38px;border-radius:5px;background:linear-gradient(180deg,var(--btn),var(--btn-dark));color:#fff;
  font-family:Ubuntu,sans-serif;font-size:15px;display:flex;align-items:center;justify-content:center;box-shadow:0 1px 2px rgba(0,0,0,.25)}

.partners{position:absolute;left:29px;top:460px;width:771px;border-top:1px dashed #999}
.partner-list{display:flex;justify-content:space-between;align-items:center;margin-top:33px;padding:0 4px}
.partner{font-weight:700;font-size:14px;color:#3a3a3a}

.site-footer{position:absolute;left:0;top:1110px;width:965px;height:90px;background:#fff}
.footer-links{position:absolute;left:92px;top:36px;font-size:12px;color:#444}
.follow{position:absolute;left:728px;top:36px;font-size:12px;color:#444;display:flex;gap:10px}
.follow b{font-weight:600;color:var(--accent)}
</style>
</head>
<body>
<div class="hero">
  <div class="hero-photo" role="img" aria-label="Photo of three smiling business professionals, a man in a pinstripe suit in front, beside a blue network cable"></div>
</div>
<div class="hero-strip"></div>

<header class="site-header">
  <div class="brand"><span class="brand-mark"></span><span class="brand-name">Marlune</span></div>
  <nav class="main-nav">
    <a class="current" href="#">Home</a>
    <a href="#">Our Services</a>
    <a href="#">About Us</a>
    <a href="#">Our Products</a>
    <a href="#">Contact Us</a>
  </nav>
</header>

<p class="hero-copy">Small Business Information Technology Services<br>Easy, Affordable and Reliable.</p>
<div class="more-btn">More</div>

<svg class="values" width="965" height="150" viewBox="0 0 965 150" aria-label="Easy, Affordable, Reliable">
  <defs>
    <filter id="soft" x="-30%" y="-30%" width="160%" height="160%"><feDropShadow dx="0" dy="1" stdDeviation="2" flood-opacity=".25"/></filter>
    <path id="arc-easy" d="M118 62 A72 72 0 0 0 262 62"/>
    <path id="arc-aff" d="M408 62 A78 78 0 0 0 564 62"/>
    <path id="arc-rel" d="M700 62 A76 76 0 0 0 852 62"/>
  </defs>
  <g filter="url(#soft)" fill="#fff">
    <circle cx="190" cy="62" r="42"/><circle cx="486" cy="62" r="42"/><circle cx="776" cy="62" r="42"/>
  </g>
  <circle cx="190" cy="62" r="21" fill="var(--badge-grey)"/>
  <circle cx="486" cy="62" r="21" fill="var(--accent)"/>
  <circle cx="776" cy="62" r="21" fill="var(--badge-grey)"/>
  <g font-family="Ubuntu, sans-serif" font-size="15" letter-spacing="2">
    <text fill="#555"><textPath href="#arc-easy" startOffset="50%" text-anchor="middle">EASY</textPath></text>
    <text fill="var(--accent)"><textPath href="#arc-aff" startOffset="50%" text-anchor="middle">AFFORDABLE</textPath></text>
    <text fill="#555"><textPath href="#arc-rel" startOffset="50%" text-anchor="middle">RELIABLE</textPath></text>
  </g>
</svg>

<main class="content-panel">
  <section class="welcome">
    <h2 class="section-title">Welcome to our site</h2>
    <div class="welcome-text">
      <p>Marlune Solutions is a computer solutions provider and IT consulting firm that supports a wide variety of local small businesses in the Calgary area primarily. Our company also provides IT services to businesses throughout Alberta on special projects.</p>
      <p>Marlune has been trusted for over the last 7 years by small business companies like yours. Whether you are looking for an ongoing computer support company, looking to outsource your small business computer work, or just looking for a computer company to help you solve a computer problem, Marlune is your right choice.</p>
      <p>We have a diversity of small business support solutions. We provide in office, over the phone, remote or drop-off computer technical support services to small business.</p>
      <p>Our computer technicians and network professionals understand that your business operations hinge on computer and network availability. Regardless if your business has one or many business locations, our preventive and ongoing business support solutions can help you keep all your computer systems running smoothly.</p>
      <p>Our computer business support services deliver unmatched reliability and expertise in computer networking, remote access, firewalls, VPNs and desktop services. Our clients enjoy that our small business support services are flexible, easy and affordable.</p>
      <p>Marlune has been recognised by many business owners for our dedication to delivering exceptional business computer support services and IT solutions. Our trained and experienced IT professionals deliver all day, and every day, rapid issue resolution, ongoing support, maintenance and stability that your business deserves and can depend upon.</p>
      <p>If you are a small business experiencing a computer or network problems or you are seeking ongoing technical support for your small business, contact us today for a free site survey and support analysis to help you find the right solution for your business.</p>
    </div>
  </section>

  <section class="quote">
    <h2 class="section-title">Submit your quote</h2>
    <div class="field">Name</div>
    <div class="field">Email Id</div>
    <div class="field">Subject</div>
    <div class="field area">Your Query</div>
    <div class="form-actions"><span class="btn">Submit</span><span class="btn">Clear</span></div>
  </section>

  <section class="partners">
    <div class="partner-list">
      <span class="partner">Quillsoft</span>
      <span class="partner">Trevo</span>
      <span class="partner">TL</span>
      <span class="partner">Brax</span>
      <span class="partner">RZO</span>
      <span class="partner">VELK</span>
      <span class="partner">Zentrix</span>
      <span class="partner">Halvor</span>
      <span class="partner">Gatemoor</span>
    </div>
  </section>
</main>

<footer class="site-footer">
  <p class="footer-links">Report Abuse | Remove Access | Powered By Plumly Pages</p>
  <p class="follow">Follow Us: <b>Pagebook</b> <b>Chirper</b></p>
</footer>
</body>
</html>
```